DEAN COLLOPY PROPERTY SERVICES

I want a business card that is clean and simple.
'Dean Collopy Property Services' is the title.
Somewhere on the card needs to be 'Carpentry, Tiling, painting and garden services'

On the back of card
PH 087 394 1526
email: deancollopypropertyservices@fernmail.net

I have attached a picture of my other business. I would like the font and design to be similar to the bathroom business.

Many thanks.

```html
<!DOCTYPE html>
<html lang="en">
<head>
<meta charset="utf-8">
<title>Dean Collopy Property Services – Business Card</title>
<link rel="stylesheet" href="https://fonts.googleapis.com/css2?family=Montserrat:wght@400;500;600&display=swap">
<style>
  :root {
    --backdrop: #999999;
    --paper: #f7f7f5;
    --ink: #2b2b2b;
    --ink-soft: #555555;
    --rule: #7a7a7a;
    --card-dark: #0c0c0c;
    --on-dark: #f4f4f4;
  }
  * { box-sizing: border-box; margin: 0; padding: 0; }
  html, body {
    width: 1200px; height: 1075px; overflow: hidden;
    background: var(--backdrop);
    font-family: "Montserrat", sans-serif;
  }
  .sheet {
    position: relative; width: 1200px; height: 1075px;
  }
  .card {
    position: absolute; left: 180px; width: 840px; height: 480px;
    border-radius: 4px;
    box-shadow: 0 18px 40px rgba(0,0,0,0.28);
  }
  .card--front { top: 40px; background: var(--paper); color: var(--ink); }
  .card--back  { top: 555px; background: var(--card-dark); color: var(--on-dark); }

  .wordmark { position: absolute; font-weight: 600; line-height: 1; white-space: nowrap; }
  .wordmark__name { display: block; letter-spacing: 0.5px; }
  .wordmark__line { display: block; letter-spacing: 3px; text-transform: uppercase; }

  .card--front .wordmark { right: 70px; top: 120px; text-align: right; color: var(--ink); }
  .card--front .wordmark__name { font-size: 44px; }
  .card--front .wordmark__line { font-size: 15px; margin-top: 8px; }

  .holder { position: absolute; left: 95px; top: 232px; }
  .holder__name { font-size: 30px; font-weight: 600; color: var(--ink); }
  .holder__role { font-size: 22px; font-weight: 400; color: var(--ink-soft); margin-top: 2px; }
  .holder__rule {
    position: absolute; left: 245px; top: 308px; width: 440px;
    height: 1.5px; background: var(--rule);
  }

  .contact { position: absolute; left: 80px; top: 330px; list-style: none; }
  .contact li {
    display: flex; align-items: center; gap: 12px;
    font-size: 22px; color: var(--ink-soft); margin-bottom: 10px;
  }
  .contact svg { width: 20px; height: 20px; fill: var(--ink); flex: none; }

  .card--back .wordmark {
    left: 0; right: 0; top: 150px; text-align: center; color: var(--on-dark);
  }
  .card--back .wordmark__name { font-size: 62px; }
  .card--back .wordmark__line { font-size: 20px; letter-spacing: 5px; margin-top: 12px; }

  .services {
    position: absolute; left: 0; right: 0; top: 330px;
    display: flex; justify-content: center; gap: 22px;
    list-style: none; font-size: 21px; font-weight: 500; color: var(--on-dark);
  }
  .services li::before { content: "•"; margin-right: 6px; }
</style>
</head>
<body>
<main class="sheet">

  <section class="card card--front" aria-label="Card front">
    <div class="wordmark">
      <span class="wordmark__name">Dean Collopy</span>
      <span class="wordmark__line">Property Services</span>
    </div>

    <div class="holder">
      <p class="holder__name">Dean Collopy</p>
      <p class="holder__role">President</p>
    </div>
    <div class="holder__rule"></div>

    <ul class="contact">
      <li>
        <svg viewBox="0 0 24 24" aria-hidden="true"><path d="M6.6 10.8a15.1 15.1 0 0 0 6.6 6.6l2.2-2.2a1 1 0 0 1 1-.25 11.4 11.4 0 0 0 3.6.57 1 1 0 0 1 1 1V20a1 1 0 0 1-1 1A17 17 0 0 1 3 4a1 1 0 0 1 1-1h3.5a1 1 0 0 1 1 1c0 1.25.2 2.45.57 3.57a1 1 0 0 1-.25 1z"/></svg>
        087 394 1526
      </li>
      <li>
        <svg viewBox="0 0 24 24" aria-hidden="true"><path d="M2 5h20v14H2z M2 5l10 7 10-7" fill="none" stroke="currentColor"/><path d="M2 5h20v2l-10 6.5L2 7z"/><path d="M2 8.5l10 6.5 10-6.5V19H2z"/></svg>
        deancollopypropertyservices@fernmail.net
      </li>
    </ul>
  </section>

  <section class="card card--back" aria-label="Card back">
    <div class="wordmark">
      <span class="wordmark__name">Dean Collopy</span>
      <span class="wordmark__line">Property Services</span>
    </div>
    <ul class="services">
      <li>Carpentry</li>
      <li>Tiling</li>
      <li>Painting and garden services</li>
    </ul>
  </section>

</main>
</body>
</html>
```